Bref créative
Keystone Assurance
Information security and compliance
Information Technology
keystoneassurance.example
We are an information technology company that specializes in auditing information security for merchants, retailers, and services providers that take credit cards and process payment transactions. We are a professional services business in information security.
Keystone Assurance should convey that we work to leverage a client’s existing systems and abilities to meet current compliance requirements. We want to convey that we will create a symbiotic relationship between organizations and compliance regulations. Symbiotic in this case bringing together two dissimilar organisms (companies) in close union with similar purpose.
Like: Clean, concise, smart. what I need.
Dislike: busy, cool, trendy cheap, template.
left side
https://www.ferrolock.example/
http://us.quorvanet.example/us/home/
http://www.brimstackgroup.example/default.html
I want to be able to update the content easily and have some type of streaming infosec related news. I want a contact page form what emails me the costumer questions/info and list my phone and email in a graphic that cannot be read by scan engines..
Tabs need to be: Home, Solutions, Industries, Contact Us. All tabs except home have options that open additional pages.
I want a clear clean font, one font type only. Colors are flexible to you artistic thoughts and my existing logo. My logo is in a few formats I like # 7 but can use different colors on other pages or formats.
I am not sure what "Nav placement" is so I selected the default. If you know better, just do it!
Logo in various formats and Styles. Some are suited for background and some color variations. Designers can be creative - I like #7 as a primary style but I am not married to that if you come up with a nice looking pages.
Continuation for log upload.
continuation of logo...

```html
<!DOCTYPE html>
<html lang="en">
<head>
<meta charset="utf-8">
<title>Keystone Assurance — Information Security and Compliance</title>
<link href="https://fonts.googleapis.com/css2?family=Arimo:wght@400;700&display=swap" rel="stylesheet">
<style>
  :root {
    --navy: #07263a;
    --teal: #0b6f93;
    --teal-light: #3ea3c6;
    --sky: #cfe6ef;
    --green: #7fb21e;
    --green-dark: #4f7d0c;
    --ink: #2b2b2b;
    --muted: #666;
    --panel: #f1f1f1;
    --line: #d3d3d3;
    --white: #fff;
  }
  * { box-sizing: border-box; margin: 0; padding: 0; }
  html, body { width: 1200px; height: 806px; overflow: hidden; }
  body {
    font-family: "Arimo", Arial, sans-serif;
    color: var(--ink);
    background: linear-gradient(90deg, #e4e4e4 0%, #fafafa 22%, #fafafa 78%, #e4e4e4 100%);
    position: relative;
  }
  .masthead {
    position: absolute; left: 0; top: 0; width: 1200px; height: 320px;
    background: linear-gradient(180deg, var(--navy) 0%, #0a3a55 30%, var(--teal) 62%, var(--teal-light) 84%, var(--sky) 100%);
  }
  .page { position: absolute; left: 264px; top: 0; width: 672px; height: 744px; }

  .brand {
    position: absolute; left: 0; top: 0; width: 264px; height: 72px;
    background: var(--white);
    display: flex; align-items: center; gap: 10px; padding-left: 18px;
  }
  .brand-mark { width: 30px; height: 30px; background: var(--teal); }
  .brand-name { color: var(--teal); font-weight: 700; font-size: 19px; text-transform: uppercase; letter-spacing: 0.5px; }

  .main-nav {
    position: absolute; left: 264px; top: 0; width: 408px; height: 30px;
    background: linear-gradient(180deg, #0d4862, #0a3046);
    border-radius: 0 0 10px 10px;
    display: flex; align-items: center; padding: 0 10px; gap: 4px;
  }
  .main-nav a {
    color: var(--white); text-decoration: none; font-size: 13px; font-weight: 700;
    padding: 6px 14px; border-right: 1px solid rgba(255,255,255,0.35); line-height: 1;
  }
  .main-nav a:last-child { border-right: none; }
  .main-nav a.is-active { background: var(--green); border-radius: 4px; border-right: none; }

  .hero {
    position: absolute; left: 0; top: 72px; width: 672px; height: 240px;
    background: linear-gradient(180deg, #d8dde2 0%, #9aa7b3 45%, #3c4650 100%);
  }

  .welcome { position: absolute; left: 0; top: 330px; width: 504px; }
  .welcome h1 { font-size: 19px; font-weight: 700; color: var(--ink); display: flex; align-items: center; gap: 8px; }
  .welcome h1 .accent { color: var(--teal); text-transform: uppercase; }
  .welcome-icon { width: 16px; height: 16px; }
  .welcome p { margin-top: 8px; font-size: 10.5px; line-height: 1.5; color: var(--muted); }

  .service-box {
    position: absolute; top: 449px; width: 240px; height: 140px;
    background: var(--panel); border: 1px solid var(--line); border-radius: 6px;
  }
  .service-box.solutions { left: 0; }
  .service-box.industries { left: 264px; }
  .service-box h2 {
    height: 28px; color: var(--white); font-size: 17px; font-weight: 700; text-align: center; line-height: 28px;
    border-radius: 6px 6px 0 0; text-transform: uppercase;
  }
  .solutions h2 { background: linear-gradient(180deg, var(--teal-light), var(--teal)); }
  .industries h2 { background: linear-gradient(180deg, #9fcd3a, var(--green-dark)); }
  .service-box .body { margin: 8px 10px 0 60px; background: var(--white); padding: 6px 8px; font-size: 9.5px; line-height: 1.4; color: var(--muted); height: 88px; }
  .service-box .body p + p { margin-top: 5px; }
  .read-more {
    position: absolute; right: 10px; bottom: 6px; background: #222; color: var(--white);
    font-size: 9.5px; padding: 3px 8px; text-decoration: none; border-radius: 2px;
  }

  .methodology { position: absolute; left: 0; top: 616px; width: 504px; }
  .methodology h2 {
    font-size: 16px; font-weight: 700; text-transform: uppercase; color: var(--ink);
    display: flex; align-items: center; gap: 10px;
  }
  .methodology h2::after { content: ""; flex: 1; height: 14px; background: linear-gradient(90deg, var(--teal), rgba(11,111,147,0)); }
  .steps { display: flex; gap: 34px; margin-top: 10px; }
  .step { width: 144px; border: 1px solid var(--line); background: var(--white); }
  .step-visual { height: 62px; }
  .step:nth-child(1) .step-visual { background: linear-gradient(135deg, #c9cdd1, #6d737a); }
  .step:nth-child(2) .step-visual { background: linear-gradient(135deg, #f6f3ea, #d9c28a); }
  .step:nth-child(3) .step-visual { background: linear-gradient(135deg, #e8e3dc, #9a8a78); }
  .step p { font-size: 10px; font-weight: 700; text-align: center; padding: 3px 0; color: var(--ink); }

  .side-panel {
    position: absolute; left: 528px; width: 144px;
    border: 1px solid var(--line); background: var(--white); border-radius: 4px;
  }
  .side-panel h2 {
    height: 26px; display: flex; align-items: center; gap: 6px; padding-left: 6px;
    color: var(--white); font-size: 14px; font-weight: 700; text-transform: uppercase;
    border-radius: 4px 4px 0 0;
  }
  .side-panel h2 .icon { width: 14px; height: 14px; background: var(--white); }
  .news { top: 331px; height: 174px; }
  .news h2 { background: linear-gradient(180deg, #9fcd3a, var(--green-dark)); }
  .news-item { padding: 6px 6px 4px; border-bottom: 1px solid #eee; font-size: 8.5px; color: var(--muted); line-height: 1.35; }
  .news-meta { display: flex; justify-content: space-between; color: var(--teal); font-weight: 700; margin-bottom: 2px; }
  .news-meta time { font-weight: 400; }
  .news-item .more { display: block; text-align: right; color: var(--green-dark); margin-top: 2px; }

  .contact { top: 523px; height: 198px; }
  .contact h2 { background: linear-gradient(180deg, var(--teal-light), var(--teal)); }
  .contact form { padding: 6px 8px; font-size: 8.5px; color: var(--muted); }
  .contact label { display: block; margin-top: 3px; }
  .contact input, .contact textarea { display: block; width: 100%; border: 1px solid #bbb; height: 13px; margin-top: 1px; }
  .contact textarea { height: 42px; resize: none; }
  .contact button {
    display: block; margin: 5px 0 0 auto; background: #222; color: var(--white); border: none;
    font-family: inherit; font-size: 9px; padding: 3px 10px;
  }

  .site-footer {
    position: absolute; left: 0; top: 744px; width: 1200px; height: 62px;
    background: linear-gradient(180deg, #a9cf4e 0%, var(--green) 40%, var(--green-dark) 100%);
  }
  .site-footer .inner { position: absolute; left: 264px; width: 672px; height: 62px; }
  .footer-links { position: absolute; left: 0; top: 18px; font-size: 9.5px; color: var(--white); }
  .footer-links a { color: var(--white); text-decoration: none; }
  .copyright { position: absolute; left: 0; top: 34px; font-size: 9.5px; color: var(--white); }
  .footer-brand { position: absolute; right: 0; top: 20px; display: flex; align-items: center; gap: 7px; }
  .footer-brand .brand-mark { width: 20px; height: 20px; background: var(--white); }
  .footer-brand span { color: var(--white); font-weight: 700; font-size: 14px; text-transform: uppercase; }
</style>
</head>
<body>
  <div class="masthead"></div>

  <div class="page">
    <div class="brand">
      <span class="brand-mark"></span>
      <span class="brand-name">Keystone Assurance</span>
    </div>

    <nav class="main-nav">
      <a href="#" class="is-active">HOME</a>
      <a href="#">SOLUTIONS</a>
      <a href="#">INDUSTRIES</a>
      <a href="#">CONTACT US</a>
    </nav>

    <div class="hero" role="img" aria-label="Photo of a team of business professionals in suits"></div>

    <section class="welcome">
      <h1>
        <svg class="welcome-icon" viewBox="0 0 16 16"><rect x="1" y="1" width="14" height="14" fill="none" stroke="#0b6f93" stroke-width="2"/><rect x="5" y="5" width="6" height="6" fill="#7fb21e"/></svg>
        Welcome to <span class="accent">Keystone Assurance</span>
      </h1>
      <p>Keystone Assurance helps merchants, retailers and service providers meet payment security standards by building on the systems and skills they already have. We audit, advise and stay alongside your team so that compliance becomes a natural part of daily work rather than a yearly scramble. Clear findings, practical steps and steady support.</p>
    </section>

    <section class="service-box solutions">
      <h2>Solutions</h2>
      <div class="body">
        <p>Security audits, gap reviews and remediation plans shaped around the tools you already run.</p>
        <p>Practical guidance that keeps every control current.</p>
      </div>
      <a href="#" class="read-more">» Read more</a>
    </section>

    <section class="service-box industries">
      <h2>Industries</h2>
      <div class="body">
        <p>Tailored compliance support for merchants, retailers, hosting firms and payment processors.</p>
        <p>Each engagement fits the way your business already works.</p>
      </div>
      <a href="#" class="read-more">» Read more</a>
    </section>

    <section class="methodology">
      <h2>Our Methodology</h2>
      <div class="steps">
        <div class="step">
          <div class="step-visual" role="img" aria-label="Photo of people at a meeting table"></div>
          <p>Understanding the Requirements</p>
        </div>
        <div class="step">
          <div class="step-visual" role="img" aria-label="Image of a rising growth chart"></div>
          <p>Service Delivery</p>
        </div>
        <div class="step">
          <div class="step-visual" role="img" aria-label="Photo of a support agent with a headset"></div>
          <p>Continuous Care</p>
        </div>
      </div>
    </section>

    <aside class="side-panel news">
      <h2><span class="icon"></span>Latest News</h2>
      <div class="news-item">
        <div class="news-meta"><span>Policy Note</span><time>20 June 2011</time></div>
        Card data rules tighten for small online merchants this quarter.
        <a href="#" class="more">» Read more</a>
      </div>
      <div class="news-item">
        <div class="news-meta"><span>Audit Tip</span><time>20 June 2011</time></div>
        New guidance on tokenisation and stored payment data released.
        <a href="#" class="more">» Read more</a>
      </div>
    </aside>

    <aside class="side-panel contact">
      <h2><span class="icon"></span>Contact Us</h2>
      <form>
        <label>Name*<input type="text"></label>
        <label>Phone*<input type="text"></label>
        <label>Email*<input type="text"></label>
        <label>Question/Comment<textarea></textarea></label>
        <button type="button">Submit</button>
      </form>
    </aside>
  </div>

  <footer class="site-footer">
    <div class="inner">
      <div class="footer-links"><a href="#">Home</a> | <a href="#">Solutions</a> | <a href="#">Industries</a> | <a href="#">Contact Us</a></div>
      <div class="copyright">Copyright © Keystone Assurance. All rights reserved.</div>
      <div class="footer-brand"><span class="brand-mark"></span><span>Keystone Assurance</span></div>
    </div>
  </footer>
</body>
</html>
```